Business Card Design

Selling beds and mattrices
See website www.lunorest.com.au for details
Targeting wholesale bed sellers

Industry/Entity Type

Business

Contact Information for Business Card

Lunorest
Director Gerald Whitcombe
Beds and Mattrices - Most technologically advanced beds in the world
European designed and made
Already No 1 seller in Europe
Call now for a quote
ph: 0472 518 306
Email: sales@lunorest.com.au
www.lunorest.com.au

```html
<!DOCTYPE html>
<html lang="en">
<head>
<meta charset="utf-8">
<title>Lunorest Business Card</title>
<link rel="stylesheet" href="https://fonts.googleapis.com/css2?family=Arimo:wght@400&display=swap">
<style>
  :root {
    --page-bg: #b9b9b9;
    --card-bg: #f7f7f7;
    --card-bg-edge: #e9e9e9;
    --ink: #111111;
    --band: #3d3d3d;
    --band-text: #ffffff;
    --bed-light: #ffffff;
    --bed-shade: #e2e2e2;
  }
  * { margin: 0; padding: 0; box-sizing: border-box; }
  html, body {
    width: 1200px; height: 900px; overflow: hidden;
    background: var(--page-bg);
    font-family: "Arimo", Arial, sans-serif;
  }
  .card {
    position: absolute; left: 100px; top: 164px;
    width: 1000px; height: 571px;
    background: linear-gradient(135deg, var(--card-bg) 0%, var(--card-bg) 55%, var(--card-bg-edge) 100%);
    box-shadow: 0 14px 30px rgba(0,0,0,.25);
    overflow: hidden;
    color: var(--ink);
  }
  .bed-visual {
    position: absolute; left: 90px; top: 200px; width: 600px; height: 290px;
    background: radial-gradient(ellipse at 55% 45%, var(--bed-light) 0%, var(--bed-light) 45%, var(--bed-shade) 100%);
    opacity: .6; border-radius: 8px;
  }
  .card-shapes { position: absolute; left: 0; top: 0; }
  .brand {
    position: absolute; left: 38px; top: 24px;
    display: flex; align-items: center; gap: 14px;
  }
  .brand-mark { width: 18px; height: 18px; background: var(--ink); }
  .brand-name {
    font-size: 66px; letter-spacing: 3px; text-transform: uppercase; line-height: 1;
  }
  .brand-region {
    position: absolute; left: 560px; top: 126px;
    font-size: 11px; letter-spacing: 1px;
  }
  .role {
    position: absolute; left: 52px; top: 166px;
    font-size: 20px; line-height: 28px;
  }
  .pitch {
    position: absolute; left: 470px; top: 176px;
    font-size: 22px; line-height: 28px;
  }
  .contact {
    position: absolute; left: 34px; top: 412px;
    font-size: 22px; line-height: 30px; color: var(--band-text);
  }
</style>
</head>
<body>
  <div class="card">
    <div class="bed-visual" role="img" aria-label="Soft white mattress photograph"></div>
    <svg class="card-shapes" width="1000" height="571" viewBox="0 0 1000 571" aria-hidden="true">
      <polygon points="740,0 1000,0 1000,130 830,130" fill="var(--band)"/>
      <polyline points="700,0 800,140 1000,140" fill="none" stroke="var(--band)" stroke-width="3"/>
      <polygon points="0,372 340,372 440,571 0,571" fill="var(--band)"/>
      <polyline points="360,372 455,545 1000,545" fill="none" stroke="var(--band)" stroke-width="3"/>
    </svg>
    <div class="brand">
      <span class="brand-mark"></span>
      <span class="brand-name">Lunorest</span>
    </div>
    <div class="brand-region">AUSTRALIA</div>
    <div class="role">
      Lunorest Director<br>
      Gerald Whitcombe<br>
      Beds and Mattrices
    </div>
    <div class="pitch">
      Most technologically advanced beds<br>
      in the world European designed and<br>
      made Already No 1 seller in Europe<br>
      Call now for a quote
    </div>
    <div class="contact">
      ph: 0472 518 306<br>
      Email: sales@lunorest.com.au<br>
      www.lunorest.com.au
    </div>
  </div>
</body>
</html>
```